Brighten Every Calling book cover and updated company logo bundle

USE THE LOGO ON THE BACK COVER. I WANT AN UPDATED LOOK TO MY LOGO
Size of book: 5.5 x 8.5
Title: Brighten Every Calling
Subtitle: An introvert’s guide to creating a coaching business that reflects who you are
The Subtitle does NOT go on the book cover
Author: Marla Toppington
BOOK DESCRIPTION: This book will help coaches and creative professionals get confidently clear on who they are so they can create a business that reflects their inner message.

DEMOGRAPHICS — Coaches and creative professional age 35-45

WOULD YOU PREFER PEOPLE OR OBJECTS ON YOUR COVER?
Objects or abstract designs
Anything I don’t want on the cover? people
Objects or symbols I want on the cover: possibly magnifying glass

IF YOU HAVE ANY PHOTOS THAT YOU WOULD LIKE US TO USE, PLEASE INCLUDE THE LINK(S) HERE. My logo or face pic for the back cover (Face pic pending)

COPY FOR THE SPINE
Brighten Every Calling
Marla Toppington
Lanternhall Books (with logo)

COPY FOR THE BACK COVER (270 words) my biz logo at the bottom and my picture next to my short bio. (Picture to come)

Create a Coaching Business that Reflects Who You Are

Do you want to step confidently into your new career by doing what you love? You aren't alone! But instead of doing what they love, many new coaches get stuck by trying to fit into traditional ways of doing business and create many unnecessary hurdles to happiness and success.
In this book, creative business coach, Marla Toppington teaches you, as she has taught herself and many others, to stop feeling guilty about what you “should” do in your life and in the process you will learn how to turn your passion into a purposeful career.

New coaches will learn how to:
• Recognize how your life decisions to this point are holding you back.
• Discover your gifts so you can express yourself through your creative projects.
• Identify and develop tools to bring your passion into purpose
• Offer services based on what you love to do.
• Understand your personal work style and work-flow to optimize your ideas and productivity.
• Create a message that reflects who you are to attract clients to work with you.
• Ask confidently for what you are worth and get it every time.
Join Marla on the journey of reconnecting with yourself and manifesting your dream.

Marla Toppington, founder of Quiet Harbor Wellness, helps new coaches and creative entrepreneurs find their inner voice so that they have the confidence to bring their authentic selves out into the world. Marla has gone through this process for herself and helped other new businesses achieve dramatic improvements in their organization and focus as a result.

Target Market(s)

indicated in description

Industry/Entity Type

Life Coaching

Logo Text

Quiet Harbor Wellness

Requirements
Must have
• updated look on existing logo it is going on the back of the book
Nice to have
• I like the font in the book cover I attached but Id like to see what else is possible

```html
<!DOCTYPE html>
<html lang="en">
<head>
<meta charset="utf-8">
<title>Brighten Every Calling — Book Cover</title>
<link href="https://fonts.googleapis.com/css2?family=Bebas+Neue&family=Zilla+Slab:wght@400;500;700&display=swap" rel="stylesheet">
<style>
  :root {
    --navy: #262845;
    --navy-soft: rgba(38, 40, 69, 0.9);
    --cream-box: rgba(246, 243, 176, 0.82);
    --cream: #f6f2b8;
    --ink: #2c2c3a;
    --title: #252842;
    --sky-blue: #2f6a8c;
    --teal: #6f9e95;
    --glow: #f2ef9e;
    --orange: #e57a2e;
    --white: #ffffff;
  }
  * { box-sizing: border-box; margin: 0; padding: 0; }
  html, body { width: 1200px; height: 888px; overflow: hidden; background: #ffffff; }
  .cover {
    position: relative; width: 1200px; height: 888px; overflow: hidden;
    font-family: "Zilla Slab", Georgia, serif; color: var(--ink);
  }
  .back {
    position: absolute; left: 0; top: 0; width: 574px; height: 888px;
    background:
      radial-gradient(ellipse 420px 260px at 290px 560px, rgba(244,240,170,0.95), rgba(244,240,170,0) 100%),
      linear-gradient(180deg, #87a898 0%, #b9c9a4 18%, #e6e6b0 40%, #ecebb2 58%, #b6b39a 70%, #4c4e6a 84%, #25274a 100%);
  }
  .spine {
    position: absolute; left: 574px; top: 0; width: 52px; height: 888px;
    background: linear-gradient(180deg, #c9d3b5 0%, #ecebbb 35%, #f1eebd 70%, #e4e1b0 100%);
  }
  .front {
    position: absolute; left: 626px; top: 0; width: 574px; height: 888px;
    background:
      radial-gradient(ellipse 360px 340px at 300px 620px, rgba(244,240,160,1), rgba(244,240,160,0) 100%),
      linear-gradient(170deg, #6c9a93 0%, #3d728f 12%, #6d9e9a 32%, #c6d29f 52%, #eeeaa6 70%, #f2eea8 100%);
  }
  .bar {
    position: absolute; left: 18px; width: 538px; height: 22px;
    background: var(--navy); color: var(--cream);
    font-size: 15px; font-weight: 500; text-align: center; line-height: 22px;
    text-transform: uppercase; letter-spacing: 0.2px;
  }
  .bar--intro { top: 55px; }
  .bar--learn { top: 311px; }
  .copy-box {
    position: absolute; left: 18px; width: 538px; background: var(--cream-box);
    font-size: 13px; line-height: 19px; padding: 4px 10px 6px 6px;
  }
  .copy-box--intro { top: 85px; height: 213px; }
  .copy-box--intro p + p { margin-top: 19px; }
  .copy-box--learn { top: 342px; height: 180px; padding: 3px 10px 4px 10px; }
  .learn-list { list-style: none; }
  .learn-list li { position: relative; padding-left: 20px; line-height: 21.7px; }
  .learn-list li::before { content: ">"; position: absolute; left: 0; font-weight: 700; }
  .author-photo {
    position: absolute; left: 18px; top: 578px; width: 102px; height: 135px;
    border: 1px solid var(--navy);
    background: linear-gradient(180deg, rgba(190,186,150,0.5), rgba(120,120,130,0.4));
  }
  .bio {
    position: absolute; left: 127px; top: 578px; width: 429px; height: 136px;
    background: var(--navy-soft); color: var(--cream);
    font-size: 14px; line-height: 22px; padding: 2px 8px;
  }
  .bio strong { font-weight: 700; }
  .business-name {
    position: absolute; left: 170px; top: 790px; width: 230px;
    display: flex; align-items: center; gap: 10px;
    color: var(--orange); font-size: 21px; font-weight: 500; line-height: 24px;
  }
  .business-name .dot { flex: none; width: 44px; height: 44px; border-radius: 50%; background: var(--orange); }
  .spine-title, .spine-author {
    position: absolute; left: 26px; white-space: nowrap; color: var(--title);
    transform-origin: 0 0; transform: rotate(90deg);
  }
  .spine-title { top: 102px; font-family: "Bebas Neue", Impact, sans-serif; font-size: 36px; line-height: 36px; margin-left: 17px; }
  .spine-author { top: 470px; font-size: 21px; line-height: 21px; font-weight: 500; margin-left: 10px; }
  .spine-publisher {
    position: absolute; left: 6px; top: 806px; width: 40px; height: 40px; border-radius: 50%;
    background: #111; color: var(--white); font-size: 6.5px; line-height: 8px;
    display: flex; align-items: center; justify-content: center; text-align: center;
  }
  .front-title {
    position: absolute; left: 0; top: 150px; width: 574px; text-align: center;
    font-family: "Bebas Neue", Impact, sans-serif; color: var(--title);
    font-size: 140px; line-height: 138px; letter-spacing: 1px;
  }
  .front-title span { display: block; }
  .lens-art {
    position: absolute; left: 290px; top: 300px; width: 110px; height: 110px; border-radius: 50%;
    background: radial-gradient(circle, rgba(245,244,205,0.9), rgba(170,180,160,0.55));
  }
  .front-author {
    position: absolute; left: 0; top: 645px; width: 574px; text-align: center;
    font-size: 39px; color: #34344a;
  }
  .front-foot { position: absolute; left: 0; bottom: 0; width: 574px; height: 50px; }
  .publisher {
    position: absolute; left: 0; bottom: 10px; width: 574px; display: flex;
    justify-content: center; align-items: center; gap: 8px;
    color: var(--white); font-size: 15px; font-weight: 700;
  }
  .publisher .dot { width: 14px; height: 14px; border-radius: 50%; background: var(--white); }
</style>
</head>
<body>
<div class="cover">
  <section class="back">
    <h2 class="bar bar--intro">Create a coaching business that reflects who you are</h2>
    <div class="copy-box copy-box--intro">
      <p>Do you want to step confidently into your new career by doing what you love? You aren't alone! But instead of doing what they love, many new coaches get stuck by trying to fit into traditional ways of doing business and create many unnecessary hurdles to happiness and success.</p>
      <p>In this book, creative business coach, Marla Toppington teaches you, as she has taught herself and many others, to stop feeling guilty about what you “should” do in your life and in the process you will learn how to turn your passion into a purposeful career.</p>
      <p>Join Marla on the journey of reconnecting with yourself and manifesting your dream.</p>
    </div>
    <h2 class="bar bar--learn">New coaches will learn how to:</h2>
    <div class="copy-box copy-box--learn">
      <ul class="learn-list">
        <li>Recognize how your life decisions to this point are holding you back.</li>
        <li>Discover your gifts so you can express yourself through your creative projects.</li>
        <li>Identify and develop tools to bring your passion into purpose.</li>
        <li>Offer services based on what you love to do.</li>
        <li>Understand your personal work style and work-flow to optimize your ideas and productivity.</li>
        <li>Create a message that reflects who you are to attract clients to work with you.</li>
        <li>Ask confidently for what you are worth and get it every time.</li>
      </ul>
    </div>
    <div class="author-photo" role="img" aria-label="Author portrait photo"></div>
    <p class="bio"><strong>Marla Toppington</strong>, founder of Quiet Harbor Wellness, helps new coaches and creative entrepreneurs find their inner voice so that they have the confidence to bring their authentic selves out into the world. Marla has gone through this process for herself and helped other new businesses achieve dramatic improvements in their organization and focus as a result.</p>
    <div class="business-name"><span class="dot"></span><span>Quiet Harbor Wellness</span></div>
  </section>

  <section class="spine">
    <div class="spine-title">BRIGHTEN EVERY CALLING</div>
    <div class="spine-author">MARLA TOPPINGTON</div>
    <div class="spine-publisher">Lanternhall Books</div>
  </section>

  <section class="front">
    <div class="lens-art" role="img" aria-label="Magnifying glass illustration"></div>
    <h1 class="front-title"><span>Brighten</span><span>Every</span><span>Calling</span></h1>
    <p class="front-author">Marla Toppington</p>
    <svg class="front-foot" width="574" height="50" viewBox="0 0 574 50" aria-hidden="true">
      <path d="M0 28 Q287 -8 574 28 L574 50 L0 50 Z" fill="#111"/>
    </svg>
    <div class="publisher"><span class="dot"></span><span>Lanternhall Books</span></div>
  </section>
</div>
</body>
</html>
```